LOGO DESIGN: Construction Related Service Business

We require a logo for our business Tovar Services. We are a construction related business offering a range of services including machine services for groundworks (digging trenches, soak wells, preparing land for construction etc), demolition and truck haulage from demolition sites.
We would like our logo to be predominately text, but may include abstract graphics. The colour scheme should be mainly a mid bright blue and overall be quite 'clean'.

Industry/Entity Type

Construction

Contact Information for Business Card

Dale Morrow
Ph:041 592 3068
tovarservices@quillnet.com.au

Colors
0456a3

```html
<!DOCTYPE html>
<html lang="en">
<head>
<meta charset="utf-8">
<title>Tovar Services – Business Card</title>
<link rel="stylesheet" href="https://fonts.googleapis.com/css2?family=Questrial&display=swap">
<style>
  :root {
    --brand-blue: #1d5a9f;
    --card-white: #f7f7f6;
    --backdrop: #e4e6e9;
    --card-shadow: rgba(0, 0, 0, 0.18);
  }
  * { box-sizing: border-box; margin: 0; padding: 0; }
  html, body {
    width: 1200px;
    height: 848px;
    overflow: hidden;
    background: var(--backdrop);
  }
  .canvas {
    position: relative;
    width: 1200px;
    height: 848px;
  }
  .business-card {
    position: absolute;
    left: 176px;
    top: 144px;
    width: 840px;
    height: 516px;
    border-radius: 30px;
    background: var(--card-white);
    box-shadow: 0 4px 14px var(--card-shadow);
    font-family: "Questrial", sans-serif;
    color: var(--brand-blue);
  }
  .wordmark {
    position: absolute;
    left: 0;
    right: 0;
    top: 118px;
    text-align: center;
  }
  .wordmark-name {
    display: block;
    font-size: 150px;
    line-height: 1;
    letter-spacing: 0.02em;
    font-weight: 400;
  }
  .wordmark-descriptor {
    display: block;
    margin-top: 6px;
    padding-left: 0.55em;
    font-size: 40px;
    line-height: 1;
    letter-spacing: 0.55em;
    font-weight: 400;
  }
  .contact-line {
    position: absolute;
    left: 17px;
    right: 17px;
    bottom: 38px;
    font-size: 23px;
    letter-spacing: 0.02em;
    white-space: nowrap;
    text-align: center;
  }
  .contact-line .divider { margin: 0 6px; }
</style>
</head>
<body>
  <main class="canvas">
    <section class="business-card" aria-label="Tovar Services business card">
      <h1 class="wordmark">
        <span class="wordmark-name">TOVAR</span>
        <span class="wordmark-descriptor">SERVICES</span>
      </h1>
      <p class="contact-line">
        <span class="contact-name">Dale Morrow</span><span class="divider">/</span><span class="contact-phone">ph:041 592 3068</span><span class="divider">/</span> <span class="contact-email">tovarservices@quillnet.com.au</span>
      </p>
    </section>
  </main>
</body>
</html>
```